Book cover Design for her new book called 'Walking a path lit by courage and grace'

My name is Velarosha, I am the founder of The Quiet Lantern.
http://velarosha-wren.shopnestle.example/
My book is an inspirational story of love and triumphing from adversity. After 40 years of surviving a life full of sexual abuse, physical and mental abuse and living with the effects of poor self-esteem and post traumatic stress disorder, this book is a guide to help others navigate away from negative emotions and help them find their own light in life. With the techniques developed and described in the book The Quiet Lantern's mission is to empower people with the journey to their own hearts and create warmth, love and inspiration.
The colours in the website represent the softness that I love and I prefer flowers. The colour also can be soft as well as vibrant and feminine. The final design should represent healing, love, inspiration and passion.

Target Market(s)

Women over the age of 25 -80
Teenagers suffering from depression
Men and women suffering from poor self esteem
Woman who have poor self confidence.

Requirements
Should not have
• Should not be dark in colour or imagery.

```html
<!DOCTYPE html>
<html lang="en">
<head>
<meta charset="utf-8">
<title>Walking a path lit by courage and grace — Velarosha</title>
<link rel="stylesheet" href="https://fonts.googleapis.com/css2?family=Cormorant+Garamond:wght@500;600;700&display=swap">
<style>
  :root {
    --sky-top: #f6f4ee;
    --sky-mist: #dcdbd3;
    --sky-grey: #cfcdc4;
    --sun-gold: #f3cf8e;
    --sky-blue: #b9dcec;
    --horizon-haze: #f1ead4;
    --field-light: #ecd08a;
    --field-gold: #d8a94f;
    --field-warm: #c59441;
    --field-base: #b9883a;
    --blossom-pink: #f1a7bf;
    --blossom-deep: #e2739a;
    --title-blue: #2f86c8;
    --author-white: #ffffff;
    --imprint-ink: #3a3a3a;
  }

  html, body {
    margin: 0;
    padding: 0;
    width: 800px;
    height: 1200px;
    overflow: hidden;
    background: #ffffff;
  }

  .book-cover {
    position: relative;
    width: 800px;
    height: 1200px;
    overflow: hidden;
    font-family: "Cormorant Garamond", Georgia, serif;
  }

  .cover-scene {
    position: absolute;
    inset: 0;
    background:
      radial-gradient(ellipse 260px 200px at 415px 40px, rgba(255,255,255,0.95), rgba(255,255,255,0) 100%),
      radial-gradient(ellipse 360px 160px at 600px 390px, rgba(243,207,142,0.85), rgba(243,207,142,0) 100%),
      radial-gradient(ellipse 380px 140px at 170px 650px, rgba(185,220,236,0.9), rgba(185,220,236,0) 100%),
      radial-gradient(ellipse 320px 200px at 420px 960px, rgba(255,240,200,0.75), rgba(255,240,200,0) 100%),
      radial-gradient(ellipse 500px 120px at 400px 800px, rgba(255,248,225,0.7), rgba(255,248,225,0) 100%),
      linear-gradient(to bottom,
        var(--sky-top) 0%,
        var(--sky-mist) 18%,
        var(--sky-grey) 30%,
        #e6dbc2 42%,
        #f2ede0 55%,
        var(--horizon-haze) 64%,
        var(--field-light) 68%,
        var(--field-gold) 80%,
        var(--field-warm) 90%,
        var(--field-base) 100%);
  }

  .blossom-branch {
    position: absolute;
    left: 0;
    top: 20px;
    width: 480px;
    height: 260px;
    background:
      radial-gradient(ellipse 180px 90px at 170px 115px, var(--blossom-pink), rgba(241,167,191,0) 100%),
      radial-gradient(ellipse 60px 40px at 360px 145px, var(--blossom-deep), rgba(226,115,154,0) 100%),
      radial-gradient(ellipse 45px 35px at 210px 205px, var(--blossom-deep), rgba(226,115,154,0) 100%);
  }

  .imprint {
    position: absolute;
    top: 84px;
    left: 0;
    width: 800px;
    text-align: center;
    font-size: 19px;
    font-weight: 600;
    letter-spacing: 0.02em;
    color: var(--imprint-ink);
  }

  .author-name {
    position: absolute;
    top: 270px;
    left: 0;
    width: 800px;
    text-align: center;
    margin: 0;
    font-size: 46px;
    font-weight: 500;
    letter-spacing: 0.14em;
    color: var(--author-white);
    text-transform: uppercase;
  }

  .book-title {
    position: absolute;
    top: 346px;
    left: 0;
    width: 800px;
    margin: 0;
    text-align: center;
    color: var(--title-blue);
    font-weight: 600;
    font-variant: small-caps;
    letter-spacing: 0.1em;
    font-size: 66px;
    line-height: 89px;
  }

  .book-title span {
    display: block;
  }

  .book-title .lead-letter {
    display: inline;
    font-size: 86px;
  }
</style>
</head>
<body>
  <main class="book-cover">
    <div class="cover-scene" role="img" aria-label="Photograph of a soft hazy sky over a golden wheat field at sunset, with a girl in a white dress walking away through the wheat"></div>
    <div class="blossom-branch" role="img" aria-label="Illustration of a pink cherry blossom branch reaching in from the top left"></div>

    <div class="imprint">The Quiet Lantern</div>

    <p class="author-name">Velarosha</p>

    <h1 class="book-title">
      <span><span class="lead-letter">W</span>alking a path</span>
      <span>lit by</span>
      <span>courage</span>
      <span>and grace</span>
    </h1>
  </main>
</body>
</html>
```